Anzeigengestaltung für Bernstein Ankaufstage in Wien
Zielgruppe
Zweck dieser Anzeige ist:
sowiele Leute wie möglich zu überzeugen, mit Ihrem Bernstein, zu uns in die Ankaufsaktion zu kommen.
Wer wir sind:
Wir sind eine Firma aus Deutschland, die sich auf die Bewertung und den Ankauf von Bernstein (Rohbernstein, Bernsteinschmuck, Kunstobjekte aus Bernstein etc. ) spezialisiert hat.
Wir führen in verschiedenen Städten Aktionen durch, in denen wir Bernstein bewerten und ggf. auch ankaufen.
Zielgruppe:
Alle leser einer Tageszeitung, Alter 50 + überwiegend ältere Damen, und generel Haushalte die Bernstein besitzen
siehe Bsp. Anzeige Wien (Datei upload)
Aufgabenstellung
Anzeigengröße B 198 mm x H 270 mm
Technische Angaben siehe PDF Tageszeitungproduktion (Datei upload)
Wir wollen auf jedenfall eine Anzeige die auch effektreich ist, nicht nur 2-dimensional und platt bleibt, sondern auch verschiedene Tiefen hat. Aber sie soll trotzdem plakativ sein.
Die Anzeige muss Seriös, Auffälig, gut lesbar, edel, frisch,..... AKTION!!
Zielgruppe ansprechen
Direkt erkennbar sein was die Anzeige bezwecken soll
Unser Hauptinteresse liegt auf den gelben ketten, davon haben wir auch 2 Bilder beigefügt.
Das wichtigste Bild ist Bild: "bernstein_2.jpg", dieses sollte schon irgendwo groß auftauchen.
Das soll auf die Anzeige:
- Textteil wie Beispielsdatei.
- AKTION
- Was....Bernstein Ankaufs-Tage in Wien
- Bernstein-Wertschätzung und Ankauf in Wien
- Wann.....vom 03.08.2017-05.08.2017
- Uhrzeit von 10:00 Uhr bis 17:00 Uhr
- Wo.... Hotel Ostara Palais, Lindauer Gasse 14, 1010 Wien, Raum: Salon 3
- Was Kaufen Wir....... Bernsteinschmuck, Bernsteinketten, Bernsteinobjekte, Rohbernsteine ab 10 g,
Bernstein Kunstgegenstände.
- Wir bieten Ihnen eine kostenlose Wertschätzung Ihrer Bernsteinstücke sowie einen
Bar-Ankauf vor Ort.
- Unser Logo
- Unsere Website www.lindwerk-handel.de
- rechts oben in der Anzeige muss das Wort -ANZEIGE- in klein stehen.
Vermerk, Achtung !!! wir kaufen nur unbehandelten Naturbernstein!!!!
siehe Bsp. Anzeige Wien bei (Datei upload)

```html
<!DOCTYPE html>
<html lang="de">
<head>
<meta charset="utf-8">
<title>Aktion Bernstein – Ankaufstage in Wien</title>
<link href="https://fonts.googleapis.com/css2?family=Montserrat:wght@400;700;800&family=Marcellus&family=Marcellus+SC&display=swap" rel="stylesheet">
<style>
:root{
  --stage:#c4c4c4;
  --amber:#f08a1c;
  --amber-light:#f7a940;
  --amber-deep:#e0700f;
  --brown-top:#5a4d4b;
  --brown-bottom:#3a2e2d;
  --ink:#2e2222;
  --text:#3b3030;
  --white:#ffffff;
}
*{margin:0;padding:0;box-sizing:border-box}
html,body{width:919px;height:1200px;overflow:hidden;background:var(--stage)}
.ad{position:absolute;left:75px;top:76px;width:772px;height:1053px;background:var(--white);overflow:hidden;box-shadow:0 3px 10px rgba(0,0,0,.35);font-family:"Marcellus",serif;color:var(--text)}
.band-top{position:absolute;left:0;top:0;width:100%;height:44px;background:linear-gradient(90deg,var(--amber-deep),var(--amber-light) 40%,var(--amber) 70%,var(--amber-deep))}
.band-bottom{position:absolute;left:0;bottom:0;width:100%;height:40px;background:linear-gradient(90deg,var(--amber-deep),var(--amber-light) 50%,var(--amber-deep))}
.dark-field{position:absolute;left:0;top:390px;width:100%;height:623px;background:linear-gradient(180deg,var(--brown-top),var(--brown-bottom))}
.label-anzeige{position:absolute;left:751px;top:100px;font-family:"Montserrat",sans-serif;font-weight:400;font-size:7px;letter-spacing:.5px;color:#777;transform:rotate(-90deg);transform-origin:left top}
.kicker{position:absolute;left:38px;top:4px;font-family:"Montserrat",sans-serif;font-weight:800;font-size:46px;line-height:40px;color:var(--white);letter-spacing:1px;white-space:nowrap}
.headline{position:absolute;left:31px;top:66px;font-family:"Montserrat",sans-serif;font-weight:800;font-size:64px;line-height:70px;white-space:nowrap;background:linear-gradient(180deg,var(--amber-light),var(--amber-deep));-webkit-background-clip:text;background-clip:text;color:transparent}
.subline{position:absolute;left:31px;top:137px;font-family:"Marcellus",serif;font-size:35px;line-height:40px;color:var(--ink);white-space:nowrap}
.photo-main{position:absolute;left:0;top:180px;width:504px;height:272px;border-radius:48% 52% 45% 40% / 55% 50% 50% 45%;background:radial-gradient(ellipse at 55% 60%,#f9b93a,#ec8d18 55%,#c8620f 85%,rgba(200,98,15,0) 100%)}
.photo-small{position:absolute;left:104px;top:908px;width:248px;height:124px;border-radius:45%;background:radial-gradient(ellipse at 50% 50%,#f6ae35,#d97617 60%,#8a4a1a 95%,rgba(138,74,26,0) 100%)}
.event{position:absolute;left:0;width:438px;text-align:center;color:var(--white);white-space:nowrap}
.event-date{top:456px;font-size:37px;line-height:44px;color:var(--amber)}
.event-time{top:505px;font-size:27px;line-height:34px}
.event-venue{top:550px;font-family:"Marcellus SC",serif;font-size:30px;line-height:36px}
.event-address{top:588px;font-size:18px;line-height:24px;letter-spacing:.3px}
.event-phone{top:620px;font-size:19px;line-height:24px;letter-spacing:.5px}
.rule{position:absolute;left:43px;width:364px;height:2px;background:var(--amber)}
.offer{position:absolute;left:0;width:440px;color:var(--white);font-size:19px;line-height:25px}
.offer-label{position:absolute;text-align:right;width:142px;left:0}
.offer-list{position:absolute;left:153px;list-style:none;white-space:nowrap}
.offer-list li{position:relative;padding-left:10px}
.offer-list li::before{content:"";position:absolute;left:0;top:10px;width:4px;height:4px;border-radius:50%;background:var(--amber)}
.article{position:absolute;left:442px;top:20px;width:295px;height:1018px;background:var(--white);border:1px solid var(--amber);box-shadow:0 0 6px rgba(0,0,0,.25);padding:12px 14px 0 14px}
.article h2{font-weight:400;font-size:20px;line-height:26px;color:var(--ink);margin-bottom:6px}
.article p{font-size:10.2px;line-height:15px;text-align:justify;hyphens:auto;-webkit-hyphens:auto;margin-bottom:13px}
.article .section-gap{margin-top:4px}
.dropcap::first-letter{float:left;font-size:32px;line-height:26px;color:var(--amber-deep);margin:2px 2px 0 0}
.brand{position:absolute;left:0;right:0;top:905px;text-align:center}
.brand-dot{display:block;width:32px;height:32px;border-radius:50%;background:var(--amber);margin:0 auto 8px}
.brand-name{font-size:20px;letter-spacing:1.5px;color:var(--text)}
.brand-web{position:absolute;left:0;right:0;top:984px;text-align:center;font-family:"Montserrat",sans-serif;font-weight:400;font-size:10px;color:#555;letter-spacing:.3px}
</style>
</head>
<body>
<div class="ad">
  <div class="band-top"></div>
  <div class="dark-field"></div>
  <div class="band-bottom"></div>
  <div class="label-anzeige">ANZEIGE</div>

  <div class="kicker">AKTION</div>
  <div class="headline">BERNSTEIN</div>
  <div class="subline">ANKAUFSTAGE in WIEN</div>

  <div class="photo-main" role="img" aria-label="Foto: gelbe Naturbernstein-Ketten in Oliven- und Kugelform"></div>

  <div class="event event-date">03.-05. August 2017</div>
  <div class="event event-time">jeweils 10-17 Uhr</div>
  <div class="event event-venue">Hotel Ostara Palais -</div>
  <div class="event event-address">Salon 3, Lindauer Gasse 14, 1010 Wien</div>
  <div class="event event-phone">T: +43 660 512 308 17</div>

  <div class="rule" style="top:662px"></div>
  <div class="offer" style="top:677px">
    <div class="offer-label">Wir bieten</div>
    <div class="offer-label" style="top:22px">Ihnen</div>
    <ul class="offer-list" style="top:22px">
      <li>kostenlose Wertschätzung<br>Ihrer Bernsteinstücke</li>
      <li>Barankauf vor Ort</li>
    </ul>
  </div>
  <div class="rule" style="top:776px"></div>
  <div class="offer" style="top:786px">
    <div class="offer-label">Wir kaufen</div>
    <ul class="offer-list">
      <li>Bernsteinschmuck</li>
      <li>Bernsteinketten</li>
      <li>Rohbernsteine ab 10 g</li>
      <li>Bernstein Kunstgegenstände</li>
    </ul>
  </div>
  <div class="rule" style="top:895px"></div>

  <div class="photo-small" role="img" aria-label="Foto: Bernsteinschmuck mit Armband, Broschen und Anhänger"></div>

  <article class="article">
    <h2>Vergessene Schätze</h2>
    <p class="dropcap">Einst als kostbare Fracht entlang der Bernsteinstraße (östliche römische Route) gelangte Bernstein von der Nord- und Ostsee nach Süden in den Mittelmeerraum. Gezeichnet durch kunstvoll gefertigte Gegenstände und allerlei Schmuck, rühmt sich das fossile Harz einer langen und vielfältigen Geschichte. Doch diese facettenreiche Geschichte scheint heute für die meisten in Vergessenheit geraten zu sein und klingt bestenfalls noch wie ein Märchen aus der Kindheit. Oft sogar als „langweilig“ oder „aus der Mode gekommen“ gebrandmarkt, wurde der Naturbernstein hier zunehmend von Juwelier-Schaufenstern und Vitrinen verbannt.</p>
    <h2 class="section-gap">Ein neues Kapitel</h2>
    <p class="dropcap">Nichtsdestoweniger wird dem Bernstein heute weltweit mehr Wertschätzung gezollt als je zuvor. Seit Neuestem wurde ein neues Kapitel aufgeschlagen. Die Bernsteinstraße, die einst gen Süden ging, führt heute bis nach China im Fernen Osten. Die aktuelle Nachfrage aus Asien hat den Handel mit Bernstein auf ganz neue Weise wiederbelebt und den Preis teilweise beträchtlich ansteigen lassen. Was mitunter in Wiener Haushalten seit Jahrzehnten in Schmuckkästchen verstaubt, wird in China als begehrtes Schmuckstück teuer gehandelt. Dort gilt Bernstein unter anderem als Symbol des Reichtums und wird stolz in der Öffentlichkeit getragen.</p>
    <h2 class="section-gap">Große Werte</h2>
    <p class="dropcap">Die Wertbestimmung für Bernstein hat sich jedoch gewandelt und abhängig von bestimmten Merkmalen variiert der Preis sehr stark. Der hier sonst sehr übliche cognacfarbene und transparente Bernsteinschmuck ist kaum mehr gefragt und in jeglicher Form behandelter oder gepresster Bernstein findet so gut wie keine Beachtung mehr. Dahingegen dominiert heute vor allem der unbehandelte naturbelassene Honigbernstein den Handel. Gelb bis orangefarbene milchige in Oliven- oder Kugelform gefertigte Ketten sind die absoluten Renner. Antike Bernsteinketten, die durch Jahrzehnte unterschiedlich stark rot bis rotbraun gefärbt wurden, sind besonders interessant. Auch sonstige Schmuckstücke, wie etwa Armbänder, Anhänger, Ringe, Broschen und andere Kleingegenstände sind beliebt. Das gilt auch für Schmuckschatullen, Schnitzereien und Kunstgegenstände aus Natur-Bernstein. Zum einen ist natürlich das Alter und der Zustand für den Preis entscheidend, aber auch Dinge wie Farbe, Größe und Marmorierung sind wichtige Faktoren. Sammler bevorzugen überwiegend gut erhaltene und antike Stücke. Es empfiehlt sich in jedem Fall einen geeigneten Fachmann zu Rate zu ziehen.</p>
    <div class="brand">
      <span class="brand-dot"></span>
      <span class="brand-name">LINDWERK</span>
    </div>
    <div class="brand-web">www.lindwerk-handel.de</div>
  </article>
</div>
</body>
</html>
```